Cutting edge GUI for a conventional C# Forms Project

I have an existing C# Forms application. The current GUI design format is Win 95 style forms. I would like to elevate the look of the software.

There are a total of six forms. Apart from two forms at 1024 X 600, the others are of different sizes. I am open to resizing them depending on the design.

I am attaching the user manual of the product to give you a better idea of what the application does. The manual also contains screenshots of individual screens. I am open to sharing the C# source files if needed.

Target Market(s)

Industrial application - Field Representatives - Will be used in Outdoor environments.

Industry/Entity Type

Software

Requirements
Must have
• A very cool, futuristic design.
Design should be light-weight as the application maybe run on net-books and low end tablets.
Should not have
• Redundant point but keep in mind that this design is going to be used in a software. So light weight is highly appreciated.

```html
<!DOCTYPE html>
<html lang="en">
<head>
<meta charset="utf-8">
<title>Diagnostics</title>
<link rel="stylesheet" href="https://fonts.googleapis.com/css2?family=Pathway+Gothic+One&family=Roboto:wght@400&display=swap">
<style>
  :root {
    --bar-dark: #3c3c3c;
    --footer-dark: #262626;
    --bg-top: #c8c8c8;
    --bg-bottom: #8a8a8a;
    --button-face: #dedede;
    --panel-dark: #565656;
    --text-dark: #1e1e1e;
    --text-light: #ffffff;
    --accent-blue: #1b97f0;
    --trace: #7ab8d0;
    --brand-green: #1f9a4c;
    --grid-minor: #ececec;
    --grid-major: #dcdcdc;
  }
  html, body { margin: 0; padding: 0; overflow: hidden; }
  .window {
    position: relative;
    width: 1200px; height: 675px;
    background: linear-gradient(180deg, var(--bg-top), var(--bg-bottom));
    font-family: "Pathway Gothic One", "Arial Narrow", sans-serif;
    overflow: hidden;
  }
  .title-bar {
    position: absolute; left: 0; top: 0; width: 1200px; height: 31px;
    background: var(--bar-dark); color: var(--text-light);
  }
  .app-mark {
    position: absolute; left: 5px; top: 4px; width: 24px; height: 23px;
    background: var(--brand-green);
  }
  .window-title {
    position: absolute; left: 37px; top: 3px;
    font-family: "Roboto", Arial, sans-serif; font-size: 20px; line-height: 24px;
  }
  .window-controls { position: absolute; right: 7px; top: 5px; display: flex; gap: 3px; }
  .window-control { width: 22px; height: 22px; display: block; }
  .chart-panel {
    position: absolute; left: 11px; top: 42px; width: 940px; height: 592px;
    background: #fff;
  }
  .side-button {
    position: absolute; left: 962px; width: 225px;
    background: var(--button-face); color: var(--text-dark);
    font-size: 21px; line-height: 27px; text-align: center;
    display: flex; align-items: center; justify-content: center;
  }
  .main-menu { top: 87px; height: 50px; }
  .sensor-check { top: 291px; height: 70px; }
  .unit-switch {
    position: absolute; left: 962px; top: 187px; width: 225px; height: 50px;
    background: var(--panel-dark); color: var(--text-light); font-size: 21px;
  }
  .unit-option { position: absolute; top: 12px; display: flex; align-items: center; gap: 12px; line-height: 26px; }
  .unit-option.mm { left: 32px; }
  .unit-option.inches { left: 124px; }
  .radio-dot { width: 15px; height: 15px; border-radius: 50%; background: #fff; box-sizing: border-box; }
  .radio-dot.selected { background: var(--accent-blue); border: 2px solid #fff; }
  .position-dial { position: absolute; left: 962px; top: 402px; width: 223px; height: 223px; }
  .status-bar {
    position: absolute; left: 0; top: 644px; width: 1200px; height: 31px;
    background: var(--footer-dark); color: var(--text-light); font-size: 21px; line-height: 31px;
  }
  .status-item { position: absolute; top: 0; white-space: nowrap; }
  .client { left: 134px; }
  .job { left: 524px; }
  .tool { left: 927px; }
</style>
</head>
<body>
<div class="window">
  <header class="title-bar">
    <span class="app-mark"></span>
    <span class="window-title">Diagnostics</span>
    <div class="window-controls">
      <svg class="window-control" viewBox="0 0 22 22"><rect width="22" height="22" fill="#f4f4f4"/><rect x="4" y="14" width="14" height="3" fill="#222"/></svg>
      <svg class="window-control" viewBox="0 0 22 22"><rect width="22" height="22" fill="#f4f4f4"/><rect x="4.5" y="5" width="13" height="12" fill="none" stroke="#222" stroke-width="2"/><rect x="4" y="4" width="14" height="3" fill="#222"/></svg>
      <svg class="window-control" viewBox="0 0 22 22"><rect width="22" height="22" fill="#f4f4f4"/><path d="M6 6 L16 16 M16 6 L6 16" stroke="#222" stroke-width="3"/></svg>
    </div>
  </header>

  <svg class="chart-panel" viewBox="0 0 940 592" aria-label="Sensor traces">
    <defs>
      <pattern id="grid-minor" width="5" height="5" patternUnits="userSpaceOnUse">
        <path d="M5 0 V5 H0" fill="none" stroke="var(--grid-minor)" stroke-width="0.6"/>
      </pattern>
      <pattern id="grid-major" width="25" height="25" patternUnits="userSpaceOnUse">
        <path d="M25 0 V25 H0" fill="none" stroke="var(--grid-major)" stroke-width="0.6"/>
      </pattern>
    </defs>
    <rect width="940" height="592" fill="url(#grid-minor)"/>
    <rect width="940" height="592" fill="url(#grid-major)"/>
    <g class="sensor-traces" fill="none" stroke="var(--trace)" stroke-width="1.6">
      <path d="M18,75 C80,68 140,82 200,74 S320,66 380,76 S500,84 560,72 L585,50 L600,78 S700,70 760,76 S860,82 922,72"/>
      <path d="M18,162 C90,154 150,168 230,158 L250,158 L262,180 L275,156 S400,150 460,162 S600,170 680,158 S820,150 922,160"/>
      <path d="M18,246 S120,256 200,244 S330,236 400,250 S480,256 520,248 C540,215 560,215 575,248 S700,256 780,244 S880,240 922,250"/>
      <path d="M18,338 S110,328 170,336 S260,346 320,334 L340,305 L355,338 S480,346 560,334 S700,326 760,338 L775,352 L790,334 S870,328 922,336"/>
      <path d="M18,420 S100,430 160,422 S280,412 350,424 S470,432 540,420 S640,414 700,426 C715,450 730,450 745,424 S860,416 922,424"/>
      <path d="M18,512 S120,502 200,510 C215,480 228,480 240,510 S360,520 430,508 S560,500 620,514 S760,520 820,506 S900,502 922,512"/>
    </g>
  </svg>

  <div class="side-button main-menu">Main menu</div>
  <div class="unit-switch" role="radiogroup" aria-label="Units">
    <span class="unit-option mm"><span class="radio-dot selected"></span>mm</span>
    <span class="unit-option inches"><span class="radio-dot"></span>inches</span>
  </div>
  <div class="side-button sensor-check">Turn off<br>sensor check</div>

  <svg class="position-dial" viewBox="0 0 223 223" aria-label="Tool orientation dial">
    <circle cx="111.5" cy="111.5" r="111" fill="#fff"/>
    <line x1="111.5" y1="111.5" x2="187" y2="186.6" stroke="var(--accent-blue)" stroke-width="2.5"/>
    <circle cx="111.5" cy="111.5" r="7" fill="#fff" stroke="var(--accent-blue)" stroke-width="2.5"/>
  </svg>

  <footer class="status-bar">
    <span class="status-item client">Northline Power</span>
    <span class="status-item job">Job number : CetB001</span>
    <span class="status-item tool">Tool Size : 6.625 inch</span>
  </footer>
</div>
</body>
</html>
```